4x6 -ish post card to let the neighborhood know where here.

Hi All, I opened a high end wine & spirits shop and am looking to get out some sort of a 4x6 postcard a flyer to let people know where in the area. Looking for something clean cut that can maybe incorporate a few pictures from our store on along the top and our logo. Ideally a white-ish background.

```html
<!DOCTYPE html>
<html lang="en">
<head>
<meta charset="utf-8">
<title>Harborstone Wine &amp; Spirits – Postcard</title>
<link href="https://fonts.googleapis.com/css2?family=Cinzel:wght@500&family=EB+Garamond:wght@400;600&family=Oswald:wght@500&display=swap" rel="stylesheet">
<style>
  :root{
    --gold:#c08a30;
    --black:#000;
    --white:#fff;
    --backdrop:#8a8a8a;
    --photo-dark:#2e3440;
    --photo-warm:#7a6a58;
  }
  *{box-sizing:border-box;margin:0;padding:0}
  html,body{width:1200px;height:863px;overflow:hidden;background:var(--backdrop)}
  body{position:relative;font-family:"EB Garamond",serif}
  .page{position:absolute;top:71px;width:480px;height:720px;overflow:hidden}
  .page--front{left:100px;background:var(--black)}
  .page--back{left:620px;background:var(--black)}
  .photo{position:absolute}
  .ring{position:absolute;border-radius:50%}
  .brand{position:absolute;font-family:"Cinzel",serif;font-weight:500;color:var(--gold);line-height:1}
  .brand__name{font-size:21px;letter-spacing:.5px;display:block}
  .brand__sub{font-size:13.5px;letter-spacing:2.2px;display:block;margin-top:4px}
  .page--back .brand__sub{color:var(--black)}
  .page--front .brand__sub{color:var(--white)}
  .heading{position:absolute;color:var(--gold);text-transform:uppercase}
  .front-heading{left:32px;top:536px;font-weight:600;font-size:16px;line-height:22px;letter-spacing:.3px}
  .features{position:absolute;left:32px;top:588px;list-style:none;color:var(--white);font-size:12.6px;line-height:15px;width:190px}
  .features li{position:relative;padding-left:20px;margin-bottom:4px}
  .features li::before{content:"";position:absolute;left:1px;top:2px;width:7px;height:11px;border:1.6px solid var(--gold);border-radius:1px;background:linear-gradient(var(--gold) 0 35%,transparent 35%)}
  .contact{position:absolute;list-style:none;font-size:9.4px;line-height:14px;white-space:nowrap}
  .contact li{display:flex;align-items:center;gap:6px}
  .contact svg{width:10px;height:10px;flex:none}
  .page--front .contact{color:var(--white)}
  .page--back .contact{color:var(--black)}
  .phone{position:absolute;height:22px;width:183px;background:var(--gold);border-radius:4px;display:flex;align-items:center;gap:5px;padding-left:4px;font-family:"Oswald",sans-serif;font-weight:500;font-size:20px;letter-spacing:1.6px;color:var(--black);line-height:1}
  .phone__icon{width:17px;height:17px;background:var(--black);border-radius:3px;display:flex;align-items:center;justify-content:center}
  .back-heading{left:47px;top:190px;font-size:24px;line-height:28px;font-weight:400;letter-spacing:.3px}
  .body-copy{position:absolute;left:47px;width:400px;color:var(--white);font-size:12.6px;line-height:15px}
</style>
</head>
<body>

<!-- Front -->
<section class="page page--front">
  <div class="photo" role="img" aria-label="Photo of the shop storefront with branded window and open door" style="left:0;top:124px;width:480px;height:400px;background:linear-gradient(160deg,#9aa0aa 0%,#5c6270 45%,#d8d8d8 70%,#8a6e5e 100%)"></div>
  <div class="ring" style="left:-31px;top:-122px;width:286px;height:286px;background:var(--gold)"></div>
  <div class="ring" style="left:-12px;top:-103px;width:248px;height:248px;background:var(--black)"></div>
  <div class="brand" style="left:45px;top:50px">
    <span class="brand__name">HARBORSTONE</span>
    <span class="brand__sub">WINE &amp; SPIRITS</span>
  </div>
  <div class="ring" style="left:215px;top:58px;width:100px;height:100px;background:var(--gold)"></div>
  <div class="photo ring" role="img" aria-label="Photo of wine bottles racked on shelves" style="left:219px;top:62px;width:92px;height:92px;border:2px solid var(--white);background:radial-gradient(circle,#6c5a50,#1e1e24)"></div>
  <div class="ring" style="left:315px;top:19px;width:142px;height:142px;background:var(--gold)"></div>
  <div class="photo ring" role="img" aria-label="Photo of a cooler stocked with canned drinks" style="left:319px;top:23px;width:134px;height:134px;border:2px solid var(--white);background:radial-gradient(circle,#5fa8d8,#1d3f6a)"></div>

  <h2 class="heading front-heading">Lorem ipsum dolor<br>sit amet,</h2>
  <ul class="features">
    <li>Lorem ipsum dolor sit amet, consectetuer adipiscing elit, sed</li>
    <li>Lorem ipsum dolor sit amet</li>
    <li>Lorem ipsum dolor sit amet, consectetuer</li>
    <li>Lorem ipsum</li>
  </ul>

  <div class="ring" style="left:214px;top:544px;width:302px;height:302px;background:var(--gold)"></div>
  <div class="ring" style="left:233px;top:563px;width:264px;height:264px;background:var(--black)"></div>
  <ul class="contact" style="left:270px;top:626px">
    <li><svg viewBox="0 0 10 10"><circle cx="5" cy="5" r="5" fill="var(--gold)"/><path d="M5 2a2 2 0 0 1 2 2c0 1.5-2 3.8-2 3.8S3 5.5 3 4a2 2 0 0 1 2-2z" fill="#000"/></svg>Lorem ipsum dolor sit amet, consectetuer</li>
    <li><svg viewBox="0 0 10 10"><circle cx="5" cy="5" r="5" fill="var(--gold)"/><rect x="2.4" y="3.2" width="5.2" height="3.6" fill="#000"/></svg>loremipsum@harborstone.com</li>
    <li><svg viewBox="0 0 10 10"><circle cx="5" cy="5" r="4.3" fill="none" stroke="var(--gold)" stroke-width="1.2"/><path d="M1 5h8M5 1c-2 2.5-2 5.5 0 8M5 1c2 2.5 2 5.5 0 8" stroke="var(--gold)" stroke-width=".8" fill="none"/></svg>www.harborstone.com</li>
  </ul>
  <div class="phone" style="left:270px;top:678px">
    <span class="phone__icon"><svg width="11" height="11" viewBox="0 0 12 12"><path d="M3 1l2 2.5-1.2 1.3c.6 1.4 1.5 2.3 2.9 2.9L8 6.5 10.5 8.5 9.5 10.5C5 10 2 7 1.5 2.5z" fill="var(--gold)"/></svg></span>000-000-0000
  </div>
</section>

<!-- Back -->
<section class="page page--back">
  <div class="photo" role="img" aria-label="Photo of the store interior with long wine aisle" style="left:200px;top:0;width:280px;height:164px;background:linear-gradient(90deg,#1c2028 0%,#8c8478 55%,#2a2e36 100%)"></div>
  <div class="ring" style="left:-30px;top:-130px;width:296px;height:296px;background:var(--gold)"></div>
  <div class="ring" style="left:-6px;top:-106px;width:248px;height:248px;background:var(--white)"></div>
  <div class="brand" style="left:48px;top:51px">
    <span class="brand__name">HARBORSTONE</span>
    <span class="brand__sub">WINE &amp; SPIRITS</span>
  </div>

  <h1 class="heading back-heading">Lorem ipsum dolor<br>sit amet,<br>consectetuer</h1>
  <p class="body-copy" style="top:282px">Lorem ipsum dolor sit amet, consectetuer adipiscing elit, sed diam nonummy nibh euismod tincidunt ut laoreet dolore magna aliquam erat volutpat. Ut wisi enim ad minim veniam, quis nostrud exerci tation ullamcorper suscipit lobortis nisl ut aliquip ex ea commodo consequat.</p>
  <p class="body-copy" style="top:358px">Duis autem vel eum iriure dolor in hendrerit in vulputate velit esse molestie consequat, vel illum dolore eu feugiat nulla facilisis at vero eros et accumsan et iusto odio dignissim qui blandit praesent luptatum zzril delenit augue duis dolore te feugait nulla facilisi.</p>

  <div class="photo" role="img" aria-label="Photo of spirits bottles on priced shelves" style="left:0;top:435px;width:480px;height:285px;background:linear-gradient(180deg,#5a4a3c 0%,#3a3a40 40%,var(--photo-warm) 70%,var(--photo-dark) 100%)"></div>
  <div class="ring" style="left:210px;top:532px;width:318px;height:318px;background:var(--gold)"></div>
  <div class="ring" style="left:229px;top:551px;width:280px;height:280px;background:var(--white)"></div>
  <ul class="contact" style="left:276px;top:626px">
    <li><svg viewBox="0 0 10 10"><path d="M5 .5a3 3 0 0 1 3 3c0 2.2-3 5.5-3 5.5S2 5.7 2 3.5a3 3 0 0 1 3-3z" fill="var(--gold)"/><circle cx="5" cy="3.5" r="1" fill="#fff"/></svg>Lorem ipsum dolor sit amet, consectetuer</li>
    <li><svg viewBox="0 0 10 10"><rect x="1.5" y="2.5" width="7" height="5" fill="var(--gold)"/><path d="M1.5 2.5L5 5.5 8.5 2.5" stroke="#fff" stroke-width=".7" fill="none"/></svg>loremipsum@harborstone.com</li>
    <li><svg viewBox="0 0 10 10"><circle cx="5" cy="5" r="4.3" fill="none" stroke="var(--gold)" stroke-width="1.2"/><path d="M1 5h8M5 1c-2 2.5-2 5.5 0 8M5 1c2 2.5 2 5.5 0 8" stroke="var(--gold)" stroke-width=".8" fill="none"/></svg>www.harborstone.com</li>
  </ul>
  <div class="phone" style="left:271px;top:678px">
    <span class="phone__icon"><svg width="11" height="11" viewBox="0 0 12 12"><path d="M3 1l2 2.5-1.2 1.3c.6 1.4 1.5 2.3 2.9 2.9L8 6.5 10.5 8.5 9.5 10.5C5 10 2 7 1.5 2.5z" fill="var(--gold)"/></svg></span>000-000-0000
  </div>
</section>

</body>
</html>
```